Disability and mental health support work company requires business card

Specialising
Wrenfield Disability is a new QCAP service aimed toward QCAP participants with a history of criminal justice, psychosocial/mental health, intellectual, and cognitive disabilities.

Our focus
Focusing on providing core QCAP supports for community participation, daily activities and supported independent living.

Authentic
Likeminded people wanting to make a difference in participant's lives.

Our aim to provide holistic and empowering supports targeted towards creating independence and guidance for all participants and families.
Over 35 years of experience working with people that have psychosocial, intellectual, and cognitive disabilities.

Industry/Entity Type

disability and mental health

Contact Information for Business Card

logo - business name

Colors
0054AA
0677BA
7BADD7
CADEEF
E8F1F8
FFF300
FFF600
FEFA6F
FFFEC7
FFFEE8

Requirements
Must have
• want double sided business cards(wont let me change it)
Should not have
• any disability related pictures

```html
<!DOCTYPE html>
<html lang="en">
<head>
<meta charset="utf-8">
<title>Wrenfield Disability – Business Card</title>
<link href="https://fonts.googleapis.com/css2?family=Arimo:wght@400;700&display=swap" rel="stylesheet">
<style>
  :root {
    --backdrop: #ebebea;
    --card-white: #fbfbfa;
    --navy: #15375f;
    --sky: #7badd7;
    --gold: #e5a91a;
    --edge-gold: #c99a1c;
    --ink: #4a4a4a;
    --rule: #6b6b6b;
  }
  * { box-sizing: border-box; margin: 0; padding: 0; }
  html, body {
    width: 1200px; height: 802px; overflow: hidden;
    background: var(--backdrop);
    font-family: "Arimo", Arial, sans-serif;
  }
  .stage {
    width: 1200px; height: 802px;
    display: flex; align-items: center; justify-content: center; gap: 60px;
  }
  .card {
    position: relative;
    width: 500px; height: 286px;
    border-bottom: 4px solid var(--edge-gold);
    box-shadow: 0 10px 24px rgba(0,0,0,0.12);
  }
  /* Front */
  .card--front { background: var(--card-white); }
  .brand-badge {
    position: absolute; top: 22px; right: 34px;
    width: 124px; height: 124px; border-radius: 50%;
    background: var(--navy);
    border: 3px solid var(--sky);
    display: flex; align-items: center; justify-content: center; text-align: center;
  }
  .brand-name {
    font-family: "Arimo", Arial, sans-serif;
    font-weight: 700; color: var(--sky);
    line-height: 1.15; letter-spacing: 0.5px;
  }
  .brand-badge .brand-name { font-size: 15px; }
  .divider {
    position: absolute; left: 30px; right: 30px; top: 168px;
    height: 1.5px; background: var(--rule);
  }
  .holder { position: absolute; left: 30px; bottom: 126px; }
  .holder-name { color: var(--gold); font-weight: 700; font-size: 26px; }
  .holder-role { color: var(--ink); font-size: 15px; margin-top: 4px; }
  .contacts {
    position: absolute; left: 30px; top: 182px;
    list-style: none; color: var(--ink); font-size: 15px;
  }
  .contacts li { display: flex; align-items: center; gap: 10px; height: 26px; }
  .contacts svg { width: 15px; height: 15px; flex: none; }
  .address {
    position: absolute; right: 30px; top: 182px;
    text-align: right; color: var(--ink); font-size: 15px; line-height: 1.45;
  }
  /* Back */
  .card--back { background: var(--navy); }
  .back-ring {
    position: absolute; top: 28px; right: 46px;
    width: 190px; height: 190px; border-radius: 50%;
    border: 3px solid var(--sky);
    display: flex; align-items: center; justify-content: center; text-align: center;
  }
  .back-ring .brand-name { font-size: 22px; }
</style>
</head>
<body>
<main class="stage">
  <section class="card card--front" aria-label="Business card front">
    <div class="brand-badge"><p class="brand-name">Wrenfield<br>Disability</p></div>
    <div class="holder">
      <p class="holder-name">Daniel Hartley</p>
      <p class="holder-role">Manager</p>
    </div>
    <div class="divider"></div>
    <ul class="contacts">
      <li>
        <svg viewBox="0 0 16 16" aria-hidden="true"><path d="M4 1.5 6.5 4 5 6c1 2 3 4 5 5l2-1.5 2.5 2.5-2 2.5C7 14 2 9 1.5 3.5z" fill="var(--gold)"/></svg>
        123-456-2100
      </li>
      <li>
        <svg viewBox="0 0 16 16" aria-hidden="true"><rect x="1.5" y="3.5" width="13" height="9" fill="none" stroke="var(--gold)" stroke-width="1.5"/><path d="M1.5 3.5 8 9l6.5-5.5" fill="none" stroke="var(--gold)" stroke-width="1.5"/></svg>
        hello@wrenfieldmail.com
      </li>
      <li>
        <svg viewBox="0 0 16 16" aria-hidden="true"><circle cx="8" cy="8" r="6.5" fill="none" stroke="var(--gold)" stroke-width="1.5"/><path d="M1.5 8h13M8 1.5c-3 3.5-3 9.5 0 13M8 1.5c3 3.5 3 9.5 0 13" fill="none" stroke="var(--gold)" stroke-width="1.2"/></svg>
        www.yourwebsite.com
      </li>
    </ul>
    <p class="address">Your address, city<br>state, ZIP 0000</p>
  </section>

  <section class="card card--back" aria-label="Business card back">
    <div class="back-ring"><p class="brand-name">Wrenfield<br>Disability</p></div>
  </section>
</main>
</body>
</html>
```